K&B RESTORATION

I want a brochure similiar to the example i've attached.
My company name is K&B Restoration. The website is: K-B-Restoration.com.
The phone number is 404.555.0173.

I don't like the "yellow" being the main color of the example so I'm open to suggestions. I want something CLEAN & Simple, like our logo . This will be a bi fold brochure

```html
<!DOCTYPE html>
<html lang="en">
<head>
<meta charset="utf-8">
<title>K&amp;B Restoration – Brochure Cover</title>
<link rel="stylesheet" href="https://fonts.googleapis.com/css2?family=Montserrat:wght@500;600;700&display=swap">
<style>
  :root {
    --page-bg: #d9d9dc;
    --cover-black: #121212;
    --cover-charcoal: #262626;
    --brand-cyan: #36b6d2;
    --brand-cyan-deep: #27a9c6;
    --ink-white: #ffffff;
  }
  html, body {
    margin: 0;
    width: 1200px;
    height: 840px;
    overflow: hidden;
    background: var(--page-bg);
    font-family: "Montserrat", sans-serif;
  }
  .cover {
    position: absolute;
    left: 324px;
    top: 30px;
    width: 552px;
    height: 780px;
    background: radial-gradient(circle at 58% 46%, var(--cover-charcoal) 0%, var(--cover-black) 60%);
    overflow: hidden;
    box-shadow: 0 18px 40px rgba(0,0,0,0.18);
  }
  .cover-shapes {
    position: absolute;
    inset: 0;
    width: 100%;
    height: 100%;
  }
  .cyan-panel { fill: url(#cyanFade); }
  .tagline-band { fill: var(--brand-cyan); }
  .wordmark {
    position: absolute;
    left: 0;
    width: 100%;
    top: 336px;
    padding-left: 90px;
    box-sizing: border-box;
    text-align: center;
    color: var(--ink-white);
    font-weight: 500;
    font-size: 32px;
    letter-spacing: 0.02em;
    margin: 0;
  }
  .tagline {
    position: absolute;
    left: 168px;
    top: 461px;
    margin: 0;
    color: var(--ink-white);
    font-weight: 700;
    font-size: 15px;
    letter-spacing: 0.14em;
    white-space: nowrap;
  }
  .tagline .dot { margin: 0 14px; }
  .website {
    position: absolute;
    left: 170px;
    top: 550px;
    margin: 0;
    color: var(--ink-white);
    font-weight: 600;
    font-size: 30px;
    white-space: nowrap;
  }
  .website .accent { color: var(--brand-cyan); }
</style>
</head>
<body>
  <main class="cover">
    <svg class="cover-shapes" viewBox="0 0 552 780" aria-hidden="true">
      <defs>
        <linearGradient id="cyanFade" x1="0" y1="0" x2="0" y2="1">
          <stop offset="0" stop-color="#46bfd6"/>
          <stop offset="1" stop-color="#27a9c6"/>
        </linearGradient>
      </defs>
      <polygon class="cyan-panel" points="0,0 171,0 36,374 199,780 0,780"/>
      <polygon class="tagline-band" points="118,437 552,437 552,507 152,507"/>
    </svg>

    <h1 class="wordmark">K&amp;B Restoration</h1>

    <p class="tagline">BUILD<span class="dot">•</span>RENOVATE<span class="dot">•</span>RESTORE</p>

    <p class="website"><span class="accent">K-B-</span>Restoration.com</p>
  </main>
</body>
</html>
```